Letterhead and Business Cards

Using our new logo we would like designs for the following,

1.Letterhead

2. 2 x Business Cards

I will need all three in high quality PDF files ready for printing. I will also require the top and bottom of the letterhead as two JPG files.

Target Market(s)

We are a business to business company dealing with middle to upper management both as clients and suppliers.

Industry/Entity Type

Business

Requirements
Must have
• 1. Look professional.
• 2. Utilise our logo colours
• 3. Incorporate our logo on both.
• 4. Letterhead

• Address:
• Kelmont Yard House
• Kelmont Yard Lane
• London
• SE9 4TQ

• Tel:0845 312 4096
• Fax: 0845 312 7041
• Website: www.quillomarket.example
• Email: info@quillomarket.example

• Directors: G.H. Pomfrey and M.R. Pomfrey Company Registration No: 52640918(This should be quite small in the letterhead footer somewhere)

• Business Card One Sided Only

• 1. Gideon H. Pomfrey
• Managing Director

• Address:
• Kelmont Yard House
• Kelmont Yard Lane
• London
• SE9 4TQ

• Tel:0845 312 4096
• Fax: 0845 312 7042
• Mob: 0791 563 2208
• Email: gideon@quillomarket.example

• 2. Miriam R. Pomfrey
• Sales Director

• Address:
• Kelmont Yard House
• Kelmont Yard Lane
• London
• SE9 4TQ

• Tel:0845 312 4096
• Fax: 0845 312 7041
• Mob: 0794 826 1159
• Email: miriam@quillomarket.example

• Please note some of this info may change for final printing.

```html
<!DOCTYPE html>
<html lang="en">
<head>
<meta charset="utf-8">
<title>Quillo Market – Business Card</title>
<link href="https://fonts.googleapis.com/css2?family=Questrial&family=Tinos&display=swap" rel="stylesheet">
<style>
  :root {
    --page-bg: #ffffff;
    --brand-green: #8cb819;
    --swoosh-grey: #a9a9a9;
    --text-grey: #8a8a8a;
    --card-edge: #5a5a5a;
    --footer-text: #ffffff;
  }
  html, body {
    margin: 0;
    padding: 0;
    width: 848px;
    height: 1200px;
    overflow: hidden;
    background: var(--page-bg);
  }
  .business-card {
    position: absolute;
    left: 247px;
    top: 497px;
    width: 368px;
    height: 225px;
    box-sizing: border-box;
    border: 0.6px solid var(--card-edge);
    background: #fff;
    overflow: hidden;
  }
  .card-swoosh {
    position: absolute;
    left: 0;
    top: 0;
    width: 368px;
    height: 225px;
  }
  .brand {
    position: absolute;
    left: 8px;
    top: 8px;
    display: flex;
    flex-direction: column;
    align-items: center;
    gap: 4px;
  }
  .brand-mark {
    width: 32px;
    height: 32px;
    border-radius: 50%;
    background: var(--brand-green);
  }
  .brand-name {
    font-family: "Questrial", sans-serif;
    font-size: 12.5px;
    color: var(--brand-green);
    white-space: nowrap;
  }
  .holder {
    position: absolute;
    left: 6px;
    top: 96px;
    width: 78px;
    text-align: right;
  }
  .holder-name {
    font-family: "Questrial", sans-serif;
    font-size: 13.6px;
    color: var(--brand-green);
    white-space: nowrap;
    text-align: left;
    line-height: 1.2;
  }
  .holder-role {
    font-family: "Tinos", serif;
    font-size: 9.5px;
    color: var(--text-grey);
    white-space: nowrap;
    line-height: 1.2;
  }
  .contact {
    position: absolute;
    right: 7px;
    top: 52px;
    text-align: right;
    font-family: "Tinos", serif;
    font-size: 11px;
    line-height: 13.8px;
    color: var(--text-grey);
    white-space: nowrap;
  }
  .contact p { margin: 0; }
  .contact .gap { height: 13.8px; }
  .card-footer {
    position: absolute;
    left: 20px;
    bottom: 10px;
    font-family: "Tinos", serif;
    font-size: 10.4px;
    color: var(--footer-text);
    white-space: nowrap;
  }
</style>
</head>
<body>
  <div class="business-card">
    <svg class="card-swoosh" viewBox="0 0 368 225" aria-hidden="true">
      <path class="swoosh-line" fill="var(--swoosh-grey)"
            d="M0,132 C120,174 230,196 300,190 Q340,187 368,176 L368,181 Q340,191 300,194 C230,200 120,181 0,142 Z"/>
      <path class="swoosh-band" fill="var(--brand-green)"
            d="M0,142 C120,181 230,200 300,194 Q340,191 368,181 L368,225 L0,225 Z"/>
    </svg>

    <div class="brand">
      <div class="brand-mark"></div>
      <div class="brand-name">Quillo Market</div>
    </div>

    <div class="holder">
      <div class="holder-name">Miriam R. Pomfrey</div>
      <div class="holder-role">Sales Director</div>
    </div>

    <div class="contact">
      <p>Address:</p>
      <p>Kelmont Yard House</p>
      <p>Kelmont Yard Lane</p>
      <p>London</p>
      <p>SE9 4TQ</p>
      <div class="gap"></div>
      <p>Tel:0845 312 4096</p>
      <p>Fax: 0845 312 7041</p>
      <p>Mob: 0794 826 1159</p>
    </div>

    <div class="card-footer">Website: www.quillomarket.example, Email: miriam@quillomarket.example</div>
  </div>
</body>
</html>
```